Zentaphone/Zentaslate App Developer Showcase Website (Redesign)

We need an attractive, modern and professional looking re-design of an existing website: www.kelvatro.com.

We have a new logo and want the website to use this - although the colors used in the logo could be altered to suit the website color scheme.

This site should consist of
- a main page showing off a few sample of apps
- a separate page for each app (one page template suitable for all apps)
- a few subsidiary pages which can be based on a single similar template, such as an About page, and Help pages for some of the apps

Note - some of the apps are Zentaphone only, and others are Zentaslate only or for both. Hence the design should allow for showing off both.

There is no need for the design to allow for lots of app screenshots (there will be links to the wareshelf where more screenshot can be seen).

It is not necessary to optimise the design just for Zentaphone screen viewing, but the
website should at least be reasonably usable on an Zentaphone and Zentaslate, as many users may be accessing the site from those devices.

Here are a few sites of similar developers - just for ideas. The first one listed is the one I think is the most attractive design. The main difference needed is that the primary function of this site is to show off the quality of the apps to app buyers, rather than to promote ourselves as app developers, which is only a secondary aim.

http://www.brindlecode.com.au/mobilebuilds.html
http://www.tarnlix.com.au/
http://www.quellomark.com/

Note - app screenshots and Zentaphone and Zentaslate device graphics templates (including glassy shadowed versions) are attached in a zip file.
Updates

Thank-you for all your submissions - your efforts are much appreciated. :-)

Seeing all the proposed designs has allowed me to see where I perhaps haven't been very clear in my brief, and also has helped me work out what type of design elements I prefer. So following is a refinement of the requirement.

The site requires only a simple layout ie.
At most it needs
- A Home page showing off a few screenshots, or with a scrolling/dynamic element, and a single link to keVTR in the wareshelf
- An About Us page
- A Contact Us page (with email form for two types are enquires a) App Support Enquiry b) Business Enquiry
- A Page for each app, including 
  > some phone/screenshot graphics
  > a description of the app features
  > a link to buy the app in the wareshelf
  > a Vidspree video demo link (for some apps only)
  > a link to a Help/FAQ page (for some apps only)

Note - if your design can show all the app info within the main page (eg. in a scrolling frame of some kind), then separate pages for each app might not even be required.

Things that are not needed are
- Request a Quote
- Follow us via Chatterfold, Peeplet etc...

Regarding the graphical design elements, I have decided that I do prefer
- designs with lighter colored backgrounds, so not black or very dark designs
- designs that keep the orange/black colors in the kelvatro logo, and use colors which work well with these

I will now contact some of you individually with specific feedback where I can - but there are so many designs already that I may not be able to contact everyone. If not, please do review your design in light of the above comments to see how well it fits.

Thanks again, and I am very pleased with results so far!

Target Market(s)

1. Zentaphone/Zentaslate owners looking for useful apps - tech savvy, well-educated
2. Companies/people looking for experienced/expert ZOS development company

Industry/Entity Type

It Professional

Requirements
Must have
• Expandable to allow new page to be added for each future apps

Use the attached new company logo design (although colors may be altered to suit website color scheme)

Site must be maintainable/expandable by ourselves once initial site is in place.
Nice to have
• Website nicely viewable from Zentaphone browser

Would be nice to have some dynamic elements eg. scrolling showcase of different app screens on main page

```html
<!DOCTYPE html>
<html lang="en">
<head>
<meta charset="utf-8">
<title>kelvatro – Zentaphone &amp; Zentaslate Apps</title>
<link href="https://fonts.googleapis.com/css2?family=Arimo:wght@400;700&display=swap" rel="stylesheet">
<style>
:root{
  --orange:#f39a12;
  --orange-dark:#e07f00;
  --ink:#1a1a1a;
  --text:#333;
  --muted:#8a8a8a;
  --heading-grey:#a9abb3;
  --line:#d9d9d9;
  --page:#ffffff;
  --band:#ececec;
  --footer:#e6e6e6;
}
*{margin:0;padding:0;box-sizing:border-box}
html,body{width:1200px;height:993px;overflow:hidden}
body{position:relative;background:var(--page);font-family:"Arimo",Arial,sans-serif;color:var(--text)}
.abs{position:absolute}

/* header */
.site-header{left:0;top:0;width:1200px;height:100px;background:linear-gradient(#fff,#f3f3f3);border-bottom:1px solid #e2e2e2;box-shadow:0 3px 6px rgba(0,0,0,.06)}
.brand{left:80px;top:26px;display:flex;align-items:center;gap:12px}
.brand-dot{width:26px;height:26px;border-radius:50%;background:var(--orange)}
.brand-name{font-size:48px;font-weight:700;color:var(--ink);letter-spacing:-1px;line-height:1}
.main-nav{top:32px;left:748px;display:flex;align-items:center}
.main-nav a{display:block;height:34px;line-height:34px;font-size:14px;color:#555;text-decoration:none;text-transform:uppercase;padding:0 14px}
.main-nav a.current{background:linear-gradient(#c4c4c4,#a9a9a9);color:#fff;border-radius:5px;width:80px;text-align:center;padding:0}
.main-nav .apps{margin-left:40px}
.main-nav .about{margin-left:27px}
.main-nav .contact{margin-left:27px}

/* hero */
.hero{left:0;top:100px;width:1200px;height:380px;background:linear-gradient(#f4f4f4,#e9e9e9 70%,#f6f6f6)}
.hero-title{left:98px;top:145px;width:560px;font-size:39px;line-height:40px;font-weight:700;color:var(--heading-grey);text-transform:uppercase}
.hero-copy{left:98px;top:240px;width:520px;font-size:14px;line-height:27px;color:var(--ink)}
.learn-more{left:107px;top:383px;width:232px;height:54px;border:1px solid #d0d0d0;border-radius:4px;background:linear-gradient(#fff,#e6e6e6);box-shadow:0 2px 4px rgba(0,0,0,.12);display:flex;align-items:center;padding-left:28px;font-size:21px;color:#333;text-transform:uppercase;text-decoration:none;letter-spacing:.5px}
.learn-more svg{position:absolute;right:12px;top:11px}
.slide-dots{left:541px;top:384px;display:flex;gap:10px;align-items:center}
.slide-dots span{width:9px;height:9px;border-radius:50%;background:var(--orange)}
.slide-dots span.active{width:20px;height:20px;background:none;border:3px solid var(--orange)}
.device-slate{left:716px;top:134px;width:396px;height:310px;border-radius:22px;background:linear-gradient(135deg,#2b2b2b,#111 60%,#3a3a3a);padding:22px}
.device-slate div{width:100%;height:100%;border-radius:4px;background:linear-gradient(#5b6f86,#8a6a58 60%,#3e4b5c)}
.device-phone{left:688px;top:216px;width:126px;height:230px;border-radius:20px;background:linear-gradient(135deg,#444,#0d0d0d);padding:30px 8px}
.device-phone div{width:100%;height:100%;border-radius:3px;background:linear-gradient(#3d5a7d,#6b7f97 50%,#2c3b4f)}

/* showcase */
.showcase-title{left:114px;top:473px;font-size:21px;color:#707070}
.showcase-title .sep{margin:0 8px}
.arrow{top:582px}
.arrow-left{left:68px}
.arrow-right{left:1095px}
.app-card{top:522px;width:141px}
.app-shot{width:141px;height:168px;border:1px solid #cfcfcf;background:#fff;padding:4px;box-shadow:0 1px 3px rgba(0,0,0,.15)}
.app-shot div{width:100%;height:100%}
.app-name{margin-top:18px;font-size:17px;color:#333}
.app-type{margin-top:8px;font-size:13px;color:#777}

/* info band */
.info-band{left:0;top:781px;width:1200px;height:145px;background:linear-gradient(#fafafa,#f0f0f0);border-top:1px solid #e0e0e0;box-shadow:0 -3px 8px rgba(0,0,0,.05)}
.band-title{top:795px;font-size:17px;color:#555;text-transform:uppercase}
.divider{top:796px;width:1px;height:112px;background:var(--line)}
.quote-mark{left:106px;top:818px;font-size:64px;line-height:1;color:#d8d8d8;font-family:Georgia,serif}
.testimonial{left:112px;top:836px;width:300px;font-size:14px;line-height:20px;color:#444}
.testimonial-author{left:302px;top:885px;font-size:14px;font-weight:700;color:#333;letter-spacing:.5px}
.newsletter-input{left:504px;top:837px;width:220px;height:29px;border:1px solid #cfcfcf;background:#fff;font-size:13px;color:#999;padding:6px 8px}
.newsletter-go{left:724px;top:837px;width:59px;height:29px;background:var(--orange);color:#fff;font-size:14px;font-weight:700;text-align:center;line-height:29px}
.radio-row{left:506px;top:877px;display:flex;gap:28px;font-size:13px;color:#555}
.radio-row span{display:flex;align-items:center;gap:7px}
.radio-row i{width:12px;height:12px;border-radius:50%;border:1px solid #999;background:#eee;display:block}
.contact-line{left:930px;font-size:13px;color:#999;line-height:18px;width:220px}
.contact-icon{left:896px}

/* footer */
.site-footer{left:0;top:926px;width:1200px;height:67px;background:var(--footer)}
.footer-links{left:68px;top:936px;font-size:12px;color:#888}
.footer-links .sep{margin:0 13px}
.copyright{left:68px;top:966px;font-size:12px;color:#888;letter-spacing:.5px}
.cards{left:987px;top:936px;display:flex;gap:8px}
.cards span{width:34px;height:21px;border-radius:3px;display:block}
</style>
</head>
<body>

<header class="site-header abs"></header>
<div class="brand abs"><span class="brand-dot"></span><span class="brand-name">kelvatro</span></div>
<nav class="main-nav abs">
  <a class="current" href="#">Home</a>
  <a class="apps" href="#">Apps</a>
  <a class="about" href="#">About</a>
  <a class="contact" href="#">Contact</a>
</nav>

<section class="hero abs"></section>
<h1 class="hero-title abs">Lorem ipsum dolor sit amet, consectetuer</h1>
<p class="hero-copy abs">Lorem ipsum dolor sit amet, consectetuer adipiscing elit. Aenean commodo ligula eget dolor. Aenean massa. Cum sociis natoque penatibus et magnis dis parturient montes, nascetur ridiculus mus. Donec quam felis, ultricies nec,</p>
<a class="learn-more abs" href="#">Learn more
  <svg width="32" height="32" viewBox="0 0 32 32"><circle cx="16" cy="16" r="15" fill="var(--orange)"/><path d="M13 10l7 6-7 6z" fill="#fff"/></svg>
</a>
<div class="slide-dots abs"><span></span><span></span><span class="active"></span></div>
<div class="device-slate abs" role="img" aria-label="Zentaslate showing the weather app forecast screen"><div></div></div>
<div class="device-phone abs" role="img" aria-label="Zentaphone showing the weather app current conditions"><div></div></div>

<h2 class="showcase-title abs">Screenshoots <span class="sep">[</span>Zentaphone<span class="sep">|</span>Zentaslate<span class="sep">]</span></h2>
<svg class="arrow arrow-left abs" width="30" height="34" viewBox="0 0 30 34"><path d="M24 2L6 17l18 15" fill="none" stroke="var(--orange)" stroke-width="7"/></svg>
<svg class="arrow arrow-right abs" width="30" height="34" viewBox="0 0 30 34"><path d="M6 2l18 15L6 32" fill="none" stroke="#cfcfcf" stroke-width="7"/></svg>

<div class="app-card abs" style="left:114px"><div class="app-shot"><div role="img" aria-label="App screenshot: city weather list" style="background:linear-gradient(#3a4f6e,#6d86a6)"></div></div><p class="app-name">Skyvane Weather</p><p class="app-type">Type: Zentaphone / Zentaslate</p></div>
<div class="app-card abs" style="left:279px"><div class="app-shot"><div role="img" aria-label="App screenshot: rain radar map" style="background:linear-gradient(#b9c8d6,#dfe3d4)"></div></div><p class="app-name">Skyvane Weather</p><p class="app-type">Type: Zentaphone / Zentaslate</p></div>
<div class="app-card abs" style="left:443px"><div class="app-shot"><div role="img" aria-label="App screenshot: wind viewer dial" style="background:radial-gradient(#2f6e6a,#111 70%)"></div></div><p class="app-name">Skyvane Weather</p><p class="app-type">Type: Zentaphone / Zentaslate</p></div>
<div class="app-card abs" style="left:608px"><div class="app-shot"><div role="img" aria-label="App screenshot: saved locations list" style="background:linear-gradient(#1c1c1c,#3b3b3b)"></div></div><p class="app-name">Skyvane Weather</p><p class="app-type">Type: Zentaphone / Zentaslate</p></div>
<div class="app-card abs" style="left:772px"><div class="app-shot"><div role="img" aria-label="App screenshot: radar sweep view" style="background:radial-gradient(#5b5a2a,#2a2418 75%)"></div></div><p class="app-name">Skyvane Weather</p><p class="app-type">Type: Zentaphone / Zentaslate</p></div>
<div class="app-card abs" style="left:937px"><div class="app-shot"><div role="img" aria-label="App screenshot: location search menu" style="background:linear-gradient(#3e5c8a,#e08a1e 45%,#e59a30)"></div></div><p class="app-name">Skyvane Weather</p><p class="app-type">Type: Zentaphone / Zentaslate</p></div>

<section class="info-band abs"></section>
<h3 class="band-title abs" style="left:111px">Testimonials</h3>
<span class="quote-mark abs">&ldquo;</span>
<p class="testimonial abs">Lorem ipsum dolor sit amet, consectetuer adipiscing e penatibus et magnis</p>
<p class="testimonial-author abs">- MARK DOWELL</p>
<span class="divider abs" style="left:422px"></span>

<h3 class="band-title abs" style="left:504px">Newsletter</h3>
<div class="newsletter-input abs">Enter Your E-mail</div>
<div class="newsletter-go abs">GO</div>
<div class="radio-row abs"><span><i></i>Subscribe</span><span><i></i>Unsubscribe</span></div>
<span class="divider abs" style="left:837px"></span>

<h3 class="band-title abs" style="left:905px">Contact us</h3>
<svg class="contact-icon abs" style="top:826px" width="14" height="14" viewBox="0 0 14 14"><path d="M3 1l3 3-2 2c1 2 2 3 4 4l2-2 3 3-2 2C6 13 1 8 1 3z" fill="#c0392b"/></svg>
<p class="contact-line abs" style="top:824px">0412 555 318</p>
<svg class="contact-icon abs" style="top:852px" width="14" height="11" viewBox="0 0 14 11"><rect width="14" height="11" fill="var(--orange)"/><path d="M0 0l7 6 7-6" fill="none" stroke="#fff" stroke-width="1.2"/></svg>
<p class="contact-line abs" style="top:848px">enquiries@kelvatro.com</p>
<svg class="contact-icon abs" style="top:875px" width="14" height="20" viewBox="0 0 14 20"><path d="M7 0a7 7 0 0 1 7 7c0 5-7 13-7 13S0 12 0 7a7 7 0 0 1 7-7z" fill="#1e90d8"/><circle cx="7" cy="7" r="2.5" fill="#fff"/></svg>
<p class="contact-line abs" style="top:874px">Lorem ipsum dolor sit amet, con-sectetuer adipiscing e</p>

<footer class="site-footer abs"></footer>
<p class="footer-links abs">Home<span class="sep">|</span>Services<span class="sep">|</span>About<span class="sep">|</span>Contact</p>
<p class="copyright abs">Copyright 2010 All rights reserved.</p>
<div class="cards abs" aria-label="Accepted payment cards">
  <span style="background:#1a3f8f"></span>
  <span style="background:#d9542b"></span>
  <span style="background:#3c8fc7"></span>
</div>

</body>
</html>
```